Brack and Loam LLC | Land Clearing, Landscaping & Dump Trailer Services

Project Description: Brack and Loam LLC Website Design
The website will be published using squarespace
Objective:
Design a visually compelling and conversion-driven website for Brack and Loam LLC, a land solutions business based in Pickens County, Georgia. The site will highlight the company’s professionalism, locally rooted service, and commitment to quality in land clearing, grading, and dump trailer services.
Pages & Features to Include:
1. Landing Page (Homepage)
- Clear tagline: Shaping Ground with Care and Grit
- Call-to-Action (CTA) buttons: “Get a Free Quote” and “View Services”
- Service highlights with icons or photos (e.g., grading, mulching, hauling)
- Customer testimonials
- Embedded contact form
- Google Maps integration showing service area
2. Services + Pricing Page
- Organized list of services under 3 categories:
- **Land Clearing & Grading**
- Forestry Mulching
- Gravel Driveway Repair
- Minimum Job Fee:
- Dump Trailer Services
- Trailer Rental (Daily):
- Junk Removal (Full Load)
- Material Delivery: $ + mileage
- Specialty Jobs
- Stump removal, light demolition
- Each service section includes short descriptions and photos
- Optional quote form at the bottom with “Request a Quote” CTA
Design Style:
- Clean, professional design using clean tones
- Fonts that balance industrial strength and local charm
- Mobile-optimized with fast loading speeds and easy navigation
- SEO-optimized for terms like *land clearing Pickens County*, *grading services North Georgia*, and *dump trailer rental Jasper GA*, etc...

```html
<!DOCTYPE html>
<html lang="en">
<head>
<meta charset="utf-8">
<title>Brack and Loam LLC | Land Clearing, Grading &amp; Hauling</title>
<link href="https://fonts.googleapis.com/css2?family=Krona+One&family=Rubik:wght@400;500;600&family=Saira:wght@500;600&display=swap" rel="stylesheet">
<style>
:root{
  --green:#4b9a34;
  --green-dark:#0d6a10;
  --green-soft:#edf3e7;
  --green-line:#9fd08a;
  --ink:#222222;
  --body:#444444;
  --charcoal:#333333;
  --charcoal-deep:#2a2a2a;
  --yellow:#f2b526;
  --white:#ffffff;
  --line:#d9d9d9;
}
*{margin:0;padding:0;box-sizing:border-box}
html,body{width:1200px;height:3950px;overflow:hidden}
body{position:relative;font-family:"Rubik",sans-serif;color:var(--body);background:var(--white)}
.display{font-family:"Krona One",sans-serif;text-transform:uppercase;color:var(--ink);letter-spacing:1px}
.abs{position:absolute}
.btn{position:absolute;display:flex;align-items:center;justify-content:center;border-radius:30px;font-family:"Krona One",sans-serif;font-size:12px;text-transform:uppercase;letter-spacing:.5px;color:var(--white);background:var(--green)}
.eyebrow{font-family:"Krona One",sans-serif;font-size:11px;text-transform:uppercase;color:var(--green);letter-spacing:1px}

/* header */
.site-header{position:absolute;left:0;top:0;width:1200px;height:76px;background:var(--white)}
.logo-name{font-family:"Krona One",sans-serif;font-size:34px;color:var(--ink);line-height:1}
.logo-sub{font-family:"Krona One",sans-serif;font-size:11.5px;color:var(--green);line-height:1;margin-top:4px}
.nav a{position:absolute;top:28px;font-family:"Krona One",sans-serif;font-size:12px;color:var(--ink);text-decoration:none}
.nav a.active{color:var(--green)}

/* hero */
.hero{position:absolute;left:0;top:76px;width:1200px;height:582px;background:linear-gradient(180deg,#3f7fb7 0%,#6aa4d0 45%,#a98a5a 80%,#6b4a2c 100%)}
.hero-title{position:absolute;left:577px;top:143px;font-size:42px;line-height:52px;color:var(--white)}
.btn-outline{background:transparent;border:2px solid var(--white)}
.hero-next{position:absolute;left:85px;top:560px;display:flex;align-items:center;gap:8px;font-family:"Krona One",sans-serif;font-size:13px;color:var(--white)}
.hero-next .rule{width:48px;height:1px;background:var(--white)}
.hero-next .ring{position:absolute;left:96px;top:-32px;width:62px;height:62px;border:1.5px solid var(--white);border-radius:50%}

/* services */
.section-head{position:absolute;left:0;width:1200px;text-align:center}
.service-card{position:absolute;top:875px;width:327px;height:430px}
.service-photo{width:327px;height:233px}
.service-body{position:absolute;left:19px;top:207px;width:290px;height:223px;background:var(--green-soft);padding:22px 34px 0}
.service-body::before{content:"";position:absolute;left:0;top:90px;width:4px;height:50px;background:var(--green)}
.service-name{display:flex;align-items:center;gap:8px;font-family:"Krona One",sans-serif;font-size:16px;color:var(--ink);text-transform:uppercase}
.service-text{font-size:13px;line-height:24px;margin-top:14px;color:var(--body)}
.service-link{display:inline-block;margin-top:10px;font-family:"Krona One",sans-serif;font-size:11.5px;color:var(--green);text-transform:uppercase;border-bottom:1.5px solid var(--green);padding-bottom:2px}

/* testimonials */
.testimonials{position:absolute;left:0;top:1441px;width:1200px;height:656px;background:var(--charcoal)}
.testi-title{position:absolute;left:85px;top:102px;font-size:36px;line-height:46px;color:var(--white)}
.arrow-btn{position:absolute;top:111px;width:46px;height:46px;border-radius:50%;display:flex;align-items:center;justify-content:center}
.testi-card{position:absolute;top:245px;width:492px;height:261px;border:1.5px solid var(--green);border-radius:12px;padding:42px 32px 0}
.testi-head{display:flex;justify-content:space-between;font-family:"Saira",sans-serif;font-size:18px;font-weight:600;color:var(--green-line)}
.stars{color:var(--yellow);letter-spacing:2px;font-size:16px}
.testi-text{margin-top:16px;font-size:16px;line-height:29px;color:#e6e6e6}
.quote-mark{position:absolute;top:-34px;left:56px;width:62px;height:52px;background:var(--charcoal)}
.testi-author{position:absolute;top:525px;display:flex;align-items:center;gap:12px}
.avatar{width:56px;height:56px;border-radius:50%;background:linear-gradient(135deg,#c9b39a,#7a5e46)}
.author-name{font-family:"Krona One",sans-serif;font-size:18px;color:var(--white);text-transform:uppercase}
.author-role{font-size:13px;color:#aaaaaa;margin-top:4px}
.dots{position:absolute;top:617px;left:556px;display:flex;gap:19px}
.dots span{width:8px;height:8px;border-radius:50%;background:#4d6f3e}
.dots span.on{background:var(--green)}

/* quote form */
.field{position:absolute;height:52px;border:1px solid var(--line);display:flex;align-items:center;gap:9px;padding-left:14px;font-size:15px;color:#666}

/* map + locations */
.map-area{position:absolute;left:0;top:2706px;width:1200px;height:498px;background:linear-gradient(135deg,#e4e4e4,#d4d4d4 50%,#e1e1e1)}
.locations{position:absolute;left:716px;top:2825px;width:398px;height:256px;background:var(--yellow);padding:50px 28px 0}
.locations .eyebrow{color:var(--white)}
.loc-title{font-size:38px;color:var(--white);margin-top:8px}
.loc-list{display:grid;grid-template-columns:180px 180px;row-gap:14px;margin-top:18px}
.loc-list span{display:flex;align-items:center;gap:8px;font-family:"Saira",sans-serif;font-weight:500;font-size:17px;color:var(--white)}

/* cta */
.cta-band{position:absolute;left:0;top:3204px;width:1200px;height:299px;background:linear-gradient(90deg,#4d9a2e 0%,#2f8a22 55%,#0b6508 100%)}
.cta-title{position:absolute;left:207px;top:91px;font-size:38px;line-height:45px;color:var(--white)}

/* footer */
.site-footer{position:absolute;left:0;top:3503px;width:1200px;height:447px;background:var(--charcoal-deep)}
.foot-col{position:absolute;top:118px}
.foot-head{font-family:"Krona One",sans-serif;font-size:12.5px;color:var(--white);text-transform:uppercase}
.foot-head::after{content:"";display:block;width:22px;height:2px;background:var(--green);margin-top:10px}
.foot-list{list-style:none;margin-top:22px}
.foot-list li{font-size:14px;color:#cfcfcf;height:35px;display:flex;align-items:center;gap:10px}
.sq{width:14px;height:14px;border-radius:3px;background:var(--green)}
.foot-about{font-size:14.5px;line-height:25px;color:#cfcfcf;margin-top:24px;width:230px}
.foot-bottom{position:absolute;left:85px;top:383px;width:1030px;border-top:1px solid #555;padding-top:24px;display:flex;justify-content:space-between;font-size:13px;color:#bbb}
.foot-bottom b{color:var(--green);font-weight:500}
</style>
</head>
<body>

<header class="site-header">
  <div class="abs" style="left:87px;top:11px">
    <div class="logo-name">BRACK</div>
    <div class="logo-sub">AND LOAM LLC</div>
  </div>
  <nav class="nav">
    <a class="active" style="left:616px" href="#">Home</a>
    <a style="left:720px" href="#">Service</a>
    <a style="left:852px" href="#">Pricing</a>
  </nav>
  <a class="btn" style="left:950px;top:11px;width:164px;height:52px">Contact</a>
</header>

<section class="hero" role="img" aria-label="Excavator bucket lifting soil on a sunny job site">
  <h1 class="display hero-title">Shaping Ground<br>with Care<br>and Grit</h1>
  <a class="btn" style="left:578px;top:330px;width:242px;height:52px">Get a free quote ↗</a>
  <a class="btn btn-outline" style="left:834px;top:330px;width:227px;height:52px">View services ↗</a>
  <div class="hero-next"><span class="rule"></span>• NEXT<span class="ring"></span></div>
</section>

<section>
  <div class="section-head" style="top:755px"><div class="eyebrow">Services</div></div>
  <div class="section-head" style="top:780px"><h2 class="display" style="font-size:38px">What we offer</h2></div>
  <div class="section-head" style="top:826px;font-size:14.5px;color:var(--ink)">Lorem ipsum dolor sit amet, coctetur adipiscing elitsit amet aliquam magn</div>

  <article class="service-card" style="left:84px">
    <div class="service-photo" role="img" aria-label="Yellow loader grading a pile of earth" style="background:linear-gradient(160deg,#5d95cf,#b7a07a 60%,#8b7655)"></div>
    <div class="service-body">
      <div class="service-name"><svg width="34" height="34" viewBox="0 0 34 34" fill="none" stroke="#4b9a34" stroke-width="2"><rect x="4" y="4" width="18" height="24" rx="2"/><path d="M8 10h10M8 15h10M8 20h6M22 20l6-6 3 3-6 6h-3z"/></svg>Grading</div>
      <p class="service-text">Lorem ipsum dolor sit amet, coctetur adipiscing elit. Vestibulum sit amet aliquam magna, at scelerisque ipsum. Sed ut posuere urna</p>
      <span class="service-link">Request a quote ↗</span>
    </div>
  </article>

  <article class="service-card" style="left:437px">
    <div class="service-photo" role="img" aria-label="Mulcher spraying wood chips among trees" style="background:linear-gradient(160deg,#5f9a3b,#9bbf5a 50%,#b9a25a)"></div>
    <div class="service-body">
      <div class="service-name"><svg width="34" height="34" viewBox="0 0 34 34" fill="none" stroke="#4b9a34" stroke-width="2"><path d="M4 6l6 2 8 14h10"/><circle cx="14" cy="27" r="3"/><path d="M10 8l12 6-4 8"/></svg>Mulching</div>
      <p class="service-text">Lorem ipsum dolor sit amet, coctetur adipiscing elit. Vestibulum sit amet aliquam magna, at scelerisque ipsum. Sed ut posuere urna</p>
      <span class="service-link">Request a quote ↗</span>
    </div>
  </article>

  <article class="service-card" style="left:788px">
    <div class="service-photo" role="img" aria-label="Dump trucks hauling gravel on a dirt road" style="background:linear-gradient(160deg,#b89a74,#d6b78e 50%,#5b8b9c)"></div>
    <div class="service-body">
      <div class="service-name"><svg width="44" height="30" viewBox="0 0 44 30" fill="#4b9a34"><rect x="2" y="6" width="24" height="14" rx="1"/><path d="M28 10h8l6 6v4H28z"/><circle cx="10" cy="24" r="4"/><circle cx="34" cy="24" r="4"/></svg>Hauling</div>
      <p class="service-text">Lorem ipsum dolor sit amet, coctetur adipiscing elit. Vestibulum sit amet aliquam magna, at scelerisque ipsum. Sed ut posuere urna</p>
      <span class="service-link">Request a quote ↗</span>
    </div>
  </article>

  <a class="btn" style="left:480px;top:1337px;width:240px;height:50px">View all services ↗</a>
</section>

<section class="testimonials">
  <div class="eyebrow abs" style="left:85px;top:76px">Testimonials</div>
  <h2 class="display testi-title">What our<br>customer says...</h2>
  <div class="arrow-btn" style="left:1013px;border:1.5px solid var(--green)"><svg width="22" height="12" viewBox="0 0 22 12" fill="none" stroke="#4b9a34" stroke-width="1.5"><path d="M21 6H1M6 1L1 6l5 5"/></svg></div>
  <div class="arrow-btn" style="left:1068px;background:var(--green)"><svg width="22" height="12" viewBox="0 0 22 12" fill="none" stroke="#fff" stroke-width="1.5"><path d="M1 6h20M16 1l5 5-5 5"/></svg></div>

  <article class="testi-card" style="left:86px">
    <div class="quote-mark"><svg width="62" height="52" viewBox="0 0 62 52" fill="#9fd08a"><path d="M2 20q0-16 16-18v9q-6 1-6 9h6v22H2z"/><path d="M34 20q0-16 16-18v9q-6 1-6 9h6v22H34z"/></svg></div>
    <div class="testi-head"><span>Great Service...</span><span class="stars">★★★★★</span></div>
    <p class="testi-text">Lorem ipsum dolor sit amet, consectetur adipiscing elit, sed do eiusmod tempor incididunt ut labore et dolore magna aliqua. Quis ipsumspendisse ultrices gravida. Risus commodo viverra maecenas accumsan lacus vel facilisis. ipsumspendisse ultrices gravida.</p>
  </article>
  <div class="testi-author" style="left:218px">
    <div class="avatar" role="img" aria-label="Client portrait"></div>
    <div><div class="author-name">Marlo Tevin</div><div class="author-role">Client</div></div>
  </div>

  <article class="testi-card" style="left:621px">
    <div class="quote-mark"><svg width="62" height="52" viewBox="0 0 62 52" fill="#9fd08a"><path d="M2 20q0-16 16-18v9q-6 1-6 9h6v22H2z"/><path d="M34 20q0-16 16-18v9q-6 1-6 9h6v22H34z"/></svg></div>
    <div class="testi-head"><span>Awesome Support...</span><span class="stars">★★★★★</span></div>
    <p class="testi-text">Lorem ipsum dolor sit amet, consectetur adipiscing elit, sed do eiusmod tempor incididunt ut labore et dolore magna aliqua. Quis ipsumspendisse ultrices gravida. Risus commodo viverra maecenas accumsan lacus vel facilisis. ipsumspendisse ultrices gravida.</p>
  </article>
  <div class="testi-author" style="left:753px">
    <div class="avatar" role="img" aria-label="Client portrait"></div>
    <div><div class="author-name">Odessa Crane</div><div class="author-role">Client</div></div>
  </div>

  <div class="dots"><span class="on"></span><span></span><span></span><span></span></div>
</section>

<section>
  <div class="abs" style="left:146px;top:2192px;width:414px;height:409px;border:1.5px solid var(--green-line);border-radius:6px"></div>
  <div class="abs" role="img" aria-label="Excavator loading an orange dump truck" style="left:129px;top:2207px;width:416px;height:410px;border-radius:6px;background:linear-gradient(160deg,#5f98d2,#9fc0dc 45%,#d69a3c 70%,#7d6a50)"></div>
  <h2 class="display abs" style="left:613px;top:2238px;font-size:38px">Get a quote</h2>
  <div class="field" style="left:612px;top:2289px;width:245px"><svg width="12" height="12" viewBox="0 0 12 12" fill="#999"><circle cx="6" cy="3.5" r="3"/><path d="M0 12q0-5 6-5t6 5z"/></svg>Name</div>
  <div class="field" style="left:869px;top:2289px;width:245px"><svg width="13" height="10" viewBox="0 0 13 10" fill="#999"><rect width="13" height="10" rx="1"/></svg>Email</div>
  <div class="field" style="left:612px;top:2353px;width:245px"><svg width="12" height="12" viewBox="0 0 12 12" fill="#999"><path d="M2 0l3 3-1.5 2q1.5 3 3.5 3.5L9 7l3 3-2 2Q1 10 0 2z"/></svg>Phone</div>
  <div class="field" style="left:869px;top:2353px;width:245px"><svg width="11" height="12" viewBox="0 0 11 12" fill="#999"><rect width="11" height="12" rx="1"/></svg>Subject</div>
  <div class="field" style="left:612px;top:2417px;width:502px;height:105px;align-items:flex-start;padding-top:12px"><svg width="12" height="12" viewBox="0 0 12 12" fill="#999" style="margin-top:6px"><path d="M0 12l1-4 7-7 3 3-7 7z"/></svg>Leave A Message</div>
  <a class="btn" style="left:613px;top:2540px;width:198px;height:51px">Submit now ↗</a>
</section>

<section class="map-area" role="img" aria-label="Map of the North Georgia service area">
  <div class="locations" style="left:716px;top:119px">
    <div class="eyebrow">Service area</div>
    <h2 class="display loc-title">Locations</h2>
    <div class="loc-list">
      <span><svg width="12" height="16" viewBox="0 0 12 16" fill="#4b9a34"><path d="M6 0a6 6 0 0 1 6 6c0 4-6 10-6 10S0 10 0 6a6 6 0 0 1 6-6z"/><circle cx="6" cy="6" r="2" fill="#f2b526"/></svg>North Georgia</span>
      <span><svg width="12" height="16" viewBox="0 0 12 16" fill="#4b9a34"><path d="M6 0a6 6 0 0 1 6 6c0 4-6 10-6 10S0 10 0 6a6 6 0 0 1 6-6z"/><circle cx="6" cy="6" r="2" fill="#f2b526"/></svg>Jasper</span>
      <span><svg width="12" height="16" viewBox="0 0 12 16" fill="#4b9a34"><path d="M6 0a6 6 0 0 1 6 6c0 4-6 10-6 10S0 10 0 6a6 6 0 0 1 6-6z"/><circle cx="6" cy="6" r="2" fill="#f2b526"/></svg>Georgia</span>
      <span><svg width="12" height="16" viewBox="0 0 12 16" fill="#4b9a34"><path d="M6 0a6 6 0 0 1 6 6c0 4-6 10-6 10S0 10 0 6a6 6 0 0 1 6-6z"/><circle cx="6" cy="6" r="2" fill="#f2b526"/></svg>Jasper</span>
    </div>
  </div>
</section>

<section class="cta-band">
  <h2 class="display cta-title">Share your<br>requirements<br>with us</h2>
  <a class="btn" style="left:734px;top:124px;width:232px;height:51px;background:#5aa63c">Request a quote ↗</a>
</section>

<footer class="site-footer">
  <div class="foot-col" style="left:87px;top:94px">
    <div class="logo-name" style="color:var(--white)">BRACK</div>
    <div class="logo-sub">AND LOAM LLC</div>
    <p class="foot-about">Lorem ipsum dolor sit coectetur adipiscing elit. Phasellus sed ultrices ligula. Sed auctor lacus et magna pulvinar porta.</p>
  </div>
  <div class="foot-col" style="left:374px">
    <div class="foot-head">Contact info</div>
    <ul class="foot-list">
      <li><svg width="13" height="13" viewBox="0 0 12 12" fill="#4b9a34"><path d="M2 0l3 3-1.5 2q1.5 3 3.5 3.5L9 7l3 3-2 2Q1 10 0 2z"/></svg>1800-555-0142</li>
      <li><svg width="14" height="11" viewBox="0 0 13 10" fill="#4b9a34"><rect width="13" height="10" rx="1"/></svg>hello@brackandloamllc.com</li>
    </ul>
  </div>
  <div class="foot-col" style="left:638px">
    <div class="foot-head">Quick links</div>
    <ul class="foot-list"><li>Home</li><li>Service</li><li>Pricing</li><li>Contact</li></ul>
  </div>
  <div class="foot-col" style="left:826px">
    <div class="foot-head">Services</div>
    <ul class="foot-list"><li>Grading</li><li>Mulching</li><li>Hauling</li><li>More..</li></ul>
  </div>
  <div class="foot-col" style="left:993px">
    <div class="foot-head">Follow us</div>
    <ul class="foot-list">
      <li><span class="sq"></span>Fieldpost</li>
      <li><span class="sq"></span>Chirpline</li>
      <li><span class="sq"></span>Snapyard</li>
      <li><span class="sq"></span>Reelhouse</li>
    </ul>
  </div>
  <div class="foot-bottom"><span>© 2025 <b>Brack and Loam LLC</b> All right reserved.</span><span>April 18, 2025, Layout_4</span></div>
</footer>

</body>
</html>
```